Law Firm Website

We are a small California based law firm specializing in business, corporate and litigation matters. We need to have our website redesigned. We are looking for a new and fresh look for our site, keeping in mind that we are a law firm.
What we don't want:
**the traditional "gavel" and "scales of justice" look
**anything too crazy
What we do want:
**sophisticated yet modern and fresh corporate look and feel
**samples of websites we really like:
http://www.tkrmllp.example
http://www.hollowaybrant.example/
we also like:
http://www.fentonardis.example/
http://www.qx.example/
http://www.moberly.example/
http://www.pvtr.example
http://www.npdlaw.example/
The content will be whatever is currently on our website (www.colterlawgroup.example). We will be selecting the winner based on originality and keeping the above requirements in mind. Please note that the photos that you use will be the ones that we will be using, so choose wisely because the photos will make a difference.
Target Market(s)
Corporate clients
Industry/Entity Type
Law Firm
Look and feel

```html
<!DOCTYPE html>
<html lang="en">
<head>
<meta charset="utf-8">
<title>Colter Law Group, LLP</title>
<link rel="stylesheet" href="https://fonts.googleapis.com/css2?family=Cormorant+SC:wght@500;600&family=Libre+Baskerville:wght@700&family=Mulish:wght@400;500&display=swap">
<style>
  :root {
    --ink-deep: #000000;
    --navy: #0a3558;
    --navy-top: #08304f;
    --bay-blue: #2f6fa8;
    --rule-grey: #2e5676;
    --accent: #1a6fc0;
    --accent-light: #5aa9f0;
    --text: #ffffff;
    --heading-grey: #a9a9a9;
    --muted: #6a6a6a;
  }
  * { margin: 0; padding: 0; box-sizing: border-box; }
  html, body { width: 1200px; height: 1187px; overflow: hidden; background: var(--ink-deep); }
  .page { position: relative; width: 1200px; height: 1187px; overflow: hidden; color: var(--text); font-family: "Mulish", sans-serif; }

  .hero-photo {
    position: absolute; left: 0; top: 0; width: 1200px; height: 800px;
    background:
      radial-gradient(ellipse 520px 260px at 830px 420px, rgba(120,180,235,.55), transparent 70%),
      radial-gradient(ellipse 300px 420px at 260px 480px, rgba(70,140,220,.45), transparent 70%),
      linear-gradient(180deg, var(--navy-top) 0%, #1d5a8c 28%, var(--bay-blue) 42%, #1a4d7c 52%, #0c2740 66%, #030a12 86%, var(--ink-deep) 100%);
  }

  .brand { position: absolute; left: 117px; top: 52px; display: flex; align-items: flex-start; gap: 16px; }
  .brand-square { width: 75px; height: 75px; background: var(--accent); }
  .brand-name { font-family: "Cormorant SC", serif; font-weight: 600; font-size: 28px; line-height: 27px; color: var(--text); margin-top: -2px; }

  .main-nav { position: absolute; left: 334px; top: 53px; width: 813px; height: 71px; border-top: 5px solid var(--rule-grey); border-bottom: 5px solid var(--rule-grey); }
  .nav-item { position: absolute; top: 16px; }
  .nav-title { display: block; font-family: "Libre Baskerville", serif; font-weight: 700; font-size: 15px; line-height: 18px; color: var(--text); }
  .nav-item.is-current .nav-title { color: var(--accent-light); }
  .nav-sub { display: block; font-size: 12px; letter-spacing: .3px; margin-top: 3px; color: var(--text); }

  .welcome { position: absolute; left: 489px; top: 548px; width: 640px; }
  .welcome h1 { font-family: "Cormorant SC", serif; font-weight: 600; font-size: 36px; line-height: 40px; letter-spacing: .3px; text-shadow: 0 1px 3px rgba(0,0,0,.6); }
  .welcome p { margin: 20px 0 0 5px; font-size: 14.5px; line-height: 22.5px; }

  .info-col { position: absolute; top: 745px; border-top: 3px solid var(--accent); padding-top: 14px; }
  .info-col h2 { font-family: "Cormorant SC", serif; font-weight: 600; font-size: 29px; line-height: 34px; color: var(--heading-grey); margin-left: 1px; }
  .info-col p, .info-col li { font-size: 14.5px; line-height: 22.5px; }
  .info-col p { margin-top: 8px; margin-left: 1px; }
  .info-col p + p { margin-top: 22.5px; }
  .practice { left: 117px; width: 310px; }
  .about { left: 489px; width: 310px; }
  .contact { left: 867px; width: 280px; }
  .practice-list { list-style: none; display: grid; grid-template-columns: 160px 1fr; margin: 22.5px 0 0 1px; }
  .more-link { display: inline-block; margin: 24px 0 0 1px; color: var(--accent); font-size: 15px; letter-spacing: .8px; text-decoration: none; }
  .more-link::after { content: "›"; margin-left: 8px; }

  .site-footer { position: absolute; left: 117px; top: 1114px; display: flex; align-items: center; }
  .social { display: flex; gap: 15px; list-style: none; }
  .social li { width: 30px; height: 30px; border-radius: 50%; background: var(--text); }
  .copyright { margin-left: 41px; font-size: 10.5px; color: var(--muted); }
</style>
</head>
<body>
<div class="page">
  <div class="hero-photo" role="img" aria-label="Night photograph of a lit suspension bridge leading to a city skyline across the bay, in blue tones"></div>

  <header>
    <div class="brand">
      <span class="brand-square"></span>
      <span class="brand-name">Colter<br>Law<br>Group</span>
    </div>
    <nav class="main-nav">
      <a class="nav-item is-current" style="left:7px"><span class="nav-title">HOME</span><span class="nav-sub">Where it begins</span></a>
      <a class="nav-item" style="left:161px"><span class="nav-title">PRACTICE AREAS</span><span class="nav-sub">What we do</span></a>
      <a class="nav-item" style="left:347px"><span class="nav-title">ABOUT</span><span class="nav-sub">Who we are</span></a>
      <a class="nav-item" style="left:504px"><span class="nav-title">LINKS</span><span class="nav-sub">How we work</span></a>
      <a class="nav-item" style="left:654px"><span class="nav-title">CONTACT</span><span class="nav-sub">When you need us</span></a>
    </nav>
  </header>

  <section class="welcome">
    <h1>Welcome to Colter Law Group, llp</h1>
    <p>Colter Law Group, LLP provides quality legal representation to corporate as well as individual clients in the areas of business, corporate, securities, products liability, civil litigation (in State and Federal Courts), Alternative Dispute Resolution (arbitration and mediation), as well as a host of transactional matters.</p>
  </section>

  <section class="info-col practice">
    <h2>Practice Areas</h2>
    <p>The key to your success is having the right team supporting you.&nbsp; Our attorneys can provide a key component: aggressive legal representation.&nbsp; We represent clients in a wide variety of fields, including:</p>
    <ul class="practice-list">
      <li>-Civil Litigation</li><li>-Mediation</li>
      <li>-Employment Law</li><li>-Corporate Securities</li>
      <li>-Arbitration</li><li>-Corporate Governance</li>
    </ul>
    <a class="more-link" href="#">VIEW FULL LIST</a>
  </section>

  <section class="info-col about">
    <h2>About Us</h2>
    <p>Our attorneys are committed to providing zeal&shy;ous advocacy in litigation, as well as creative approaches to difficult challenges that face our business clients.</p>
    <p>Our goal is to provide the highest level of rep&shy;resentation and personal service to each and every client, and to meet and exceed each client's expectations.</p>
    <a class="more-link" href="#">READ MORE</a>
  </section>

  <section class="info-col contact">
    <h2>Contact Us</h2>
    <p>ALDERTON OFFICE<br>4150 Meridian Park Drive, 8th Floor<br>Alderton, California 92600</p>
    <p>Telephone: (555) 014-2200<br>Facsimile:&nbsp;&nbsp;&nbsp;(555) 014-2277</p>
    <p>info@colterlawgroup.example</p>
    <a class="more-link" href="#">READ MORE</a>
  </section>

  <footer class="site-footer">
    <ul class="social">
      <li aria-label="Social profile"></li>
      <li aria-label="Social profile"></li>
      <li aria-label="Social profile"></li>
      <li aria-label="News feed"></li>
    </ul>
    <p class="copyright">Copyright 2014 © Colter Law Group, LLP - All Rights Reserved. Site Map | Privacy Policy</p>
  </footer>
</div>
</body>
</html>
```